Bref créative
KTR stationery
Simple
Samir Haddoud
Managing Director
Dubai Office:
P.O. Box 48213, Dubai, UAE
T: +971 4 5708812
Beirut Office:
Solvira Hotel & Resort - Corniche
Rue des Tilleuls Avenue
Zaitouné 4157 2203, Beirut, Lebanon
T: +961 1 537204
samir@koratecholding.example
www.koratecholding.example
directly under name and title, pls put
M: +971 55 8064139

```html
<!DOCTYPE html>
<html lang="en">
<head>
<meta charset="utf-8">
<title>KTR Stationery</title>
<link rel="stylesheet" href="https://fonts.googleapis.com/css2?family=Open+Sans:wght@400;600;700&display=swap">
<style>
:root{
  --bg:#e4e6ea;
  --paper:#ffffff;
  --blue:#1f80d2;
  --blue-dark:#1565b0;
  --blue-pale:#e6eef9;
  --red:#c8202e;
  --ink:#3c4047;
  --muted:#8a9099;
  --cell:#e3e5e8;
}
*{box-sizing:border-box;margin:0;padding:0}
html,body{width:1200px;height:835px;overflow:hidden}
body{background:var(--bg);font-family:"Open Sans",Arial,sans-serif;color:var(--ink);position:relative}
.sheet{position:absolute;background:var(--paper);box-shadow:0 3px 10px rgba(0,0,0,.18);overflow:hidden}
.brand{display:flex;align-items:center;gap:6px}
.brand-square{width:10px;height:10px;background:var(--blue)}
.brand-name{font-weight:700;color:var(--red);letter-spacing:1px}
.brand-sub{font-size:5.5px;color:var(--muted);letter-spacing:1.5px;text-transform:uppercase;margin-top:2px}
.ghost-name{position:absolute;font-weight:700;color:var(--blue-pale);letter-spacing:4px;line-height:1}
.band{position:absolute;left:0;right:0;bottom:0;background:linear-gradient(90deg,var(--blue-dark),var(--blue))}

/* letterhead */
.letterhead{left:40px;top:134px;width:400px;height:566px}
.letterhead .brand{position:absolute;left:34px;top:36px}
.letterhead .brand-name{font-size:26px}
.letterhead .ghost-name{right:-20px;top:40px;font-size:120px}
.letterhead .contact{position:absolute;left:34px;top:470px;font-size:6px;line-height:1.55;color:var(--ink);display:flex;gap:28px}
.contact strong{color:var(--blue);font-weight:600}
.letterhead .band{height:12px}

/* fax */
.fax{left:470px;top:134px;width:400px;height:566px}
.fax .brand{position:absolute;left:34px;top:36px}
.fax .brand-name{font-size:26px}
.fax-title{position:absolute;right:34px;top:40px;font-size:22px;font-weight:700;color:var(--muted);letter-spacing:6px}
.fax-table{position:absolute;left:34px;top:110px;width:332px;border-collapse:collapse;font-size:7px}
.fax-table td{border:2px solid var(--paper);height:22px;padding:0 8px}
.fax-table .label{background:var(--cell);width:56px;font-weight:600;color:var(--ink)}
.fax-table .field{background:#f3f4f6}
.fax-checks{position:absolute;left:34px;top:220px;display:flex;gap:22px;font-size:7px}
.fax-checks span{display:flex;align-items:center;gap:5px}
.fax-checks i{width:8px;height:8px;border:1px solid var(--muted);display:inline-block}
.fax-lines{position:absolute;left:34px;right:34px;top:260px}
.fax-lines div{border-bottom:1px solid #edeef0;height:22px}
.fax .ghost-name{right:-20px;top:330px;font-size:120px}
.fax .band{height:12px}

/* envelopes */
.env-front{left:900px;top:107px;width:260px;height:130px}
.env-front .brand{position:absolute;left:16px;top:14px}
.env-front .brand-name{font-size:16px}
.env-front .return{position:absolute;left:16px;top:48px;font-size:5px;line-height:1.5;color:var(--muted)}
.env-front .band{height:8px}
.env-back{left:900px;top:257px;width:260px;height:130px}
.env-back svg{position:absolute;inset:0}
.env-back .flap-name{position:absolute;left:0;right:0;top:24px;text-align:center;font-size:14px;font-weight:700;color:#fff;letter-spacing:2px}

/* cards */
.card{width:260px;height:150px}
.card-front{left:900px;top:407px}
.card-front .brand{position:absolute;left:16px;top:14px}
.card-front .brand-name{font-size:17px}
.card-front .person{position:absolute;right:16px;top:16px;text-align:right}
.person .name{font-size:9px;font-weight:700;color:var(--blue)}
.person .title{font-size:6.5px;color:var(--muted)}
.person .mobile{font-size:6.5px;color:var(--ink);margin-top:2px}
.card-front .details{position:absolute;left:16px;top:60px;right:16px;display:flex;justify-content:space-between;font-size:5.4px;line-height:1.5}
.card-front .web{position:absolute;left:16px;bottom:14px;font-size:5.6px;color:var(--ink)}
.card-front .band{height:6px}
.card-back{left:900px;top:577px;background:linear-gradient(135deg,var(--blue),var(--blue-dark));display:flex;align-items:center;justify-content:center}
.card-back .brand-name{font-size:26px;color:#fff;letter-spacing:4px}
</style>
</head>
<body>

<section class="sheet letterhead">
  <div class="ghost-name">KTR</div>
  <div class="brand">
    <div class="brand-square"></div>
    <div><div class="brand-name">KTR</div><div class="brand-sub">Koratec Holding</div></div>
  </div>
  <div class="contact">
    <div><strong>Dubai Office:</strong><br>P.O. Box 48213, Dubai, UAE<br>T: +971 4 5708812</div>
    <div><strong>Beirut Office:</strong><br>Solvira Hotel &amp; Resort - Corniche<br>Rue des Tilleuls Avenue<br>Zaitouné 4157 2203, Beirut, Lebanon<br>T: +961 1 537204</div>
    <div>samir@koratecholding.example<br>www.koratecholding.example</div>
  </div>
  <div class="band"></div>
</section>

<section class="sheet fax">
  <div class="brand">
    <div class="brand-square"></div>
    <div><div class="brand-name">KTR</div><div class="brand-sub">Koratec Holding</div></div>
  </div>
  <div class="fax-title">FAX</div>
  <table class="fax-table">
    <tr><td class="label">To</td><td class="field"></td><td class="label">From</td><td class="field"></td></tr>
    <tr><td class="label">Fax</td><td class="field"></td><td class="label">Phone</td><td class="field"></td></tr>
    <tr><td class="label">Date</td><td class="field"></td><td class="label">Pages</td><td class="field"></td></tr>
    <tr><td class="label">Subject</td><td class="field" colspan="3"></td></tr>
  </table>
  <div class="fax-checks">
    <span><i></i>Urgent</span><span><i></i>For Review</span><span><i></i>Please Reply</span>
  </div>
  <div class="fax-lines"><div></div><div></div><div></div><div></div><div></div><div></div><div></div><div></div><div></div><div></div></div>
  <div class="ghost-name">KTR</div>
  <div class="band"></div>
</section>

<section class="sheet env-front">
  <div class="brand">
    <div class="brand-square"></div>
    <div class="brand-name">KTR</div>
  </div>
  <div class="return">P.O. Box 48213, Dubai, UAE<br>www.koratecholding.example</div>
  <div class="band"></div>
</section>

<section class="sheet env-back">
  <svg width="260" height="130" viewBox="0 0 260 130" aria-hidden="true">
    <defs>
      <linearGradient id="flapFill" x1="0" y1="0" x2="1" y2="1">
        <stop offset="0" stop-color="#1f80d2"/><stop offset="1" stop-color="#1565b0"/>
      </linearGradient>
    </defs>
    <path d="M0 0 H260 L130 72 Z" fill="url(#flapFill)"/>
    <path d="M0 130 L110 62 M260 130 L150 62" stroke="#e3e6ea" stroke-width="1" fill="none"/>
  </svg>
  <div class="flap-name">KTR</div>
</section>

<section class="sheet card card-front">
  <div class="brand">
    <div class="brand-square"></div>
    <div class="brand-name">KTR</div>
  </div>
  <div class="person">
    <div class="name">Samir Haddoud</div>
    <div class="title">Managing Director</div>
    <div class="mobile">M: +971 55 8064139</div>
  </div>
  <div class="details">
    <div><strong style="color:var(--blue)">Dubai Office:</strong><br>P.O. Box 48213, Dubai, UAE<br>T: +971 4 5708812</div>
    <div><strong style="color:var(--blue)">Beirut Office:</strong><br>Solvira Hotel &amp; Resort - Corniche<br>Rue des Tilleuls Avenue<br>Zaitouné 4157 2203, Beirut, Lebanon<br>T: +961 1 537204</div>
  </div>
  <div class="web">samir@koratecholding.example &nbsp;|&nbsp; www.koratecholding.example</div>
  <div class="band"></div>
</section>

<section class="sheet card card-back">
  <div class="brand-name">KTR</div>
</section>

</body>
</html>
```